We are a Leadership Specialist Boutique Business that is launching a residential womans workshop....

We need a post card which will include our logo, an overview of our workshop, a catch statement on one side and on the other side dates, venue, facilitators and contacts to book the workshop. The postcards will be distributed at an Global Sisterhood Harvest Lunch. They will be placed at each setting of the lunch attendees. The company QBR running the lunch is a sponsor of our business.

Target Market(s)

Women supervisor to middle management positions or own business

Industry/Entity Type

Academic Training

Font styles to use
Serif

Colors
34a7d8

Requirements
Must have
• Use Colour Palette on docs attached, Logo, Workshop overview either the Circle Theory or the Core Philosophy Text,
• The dates, venue, all costs of the program including discount code. One catch sentence that grabs the audience from the content I have provided that appeals to the designer
• Must have these contacts.
• Website: brightpathforwardgroup.com,au
• Email: Info@brightpathforwardgroup.com.au.
• Phone: 0419372605
Nice to have
• Facilitators Photos and names

```html
<!DOCTYPE html>
<html lang="en">
<head>
<meta charset="utf-8">
<title>Bright Path – Residential Women's Workshop Postcard</title>
<link rel="stylesheet" href="https://fonts.googleapis.com/css2?family=Exo+2:wght@400;500;700;800&family=Roboto+Condensed:wght@400;700&display=swap">
<style>
:root{
  --teal:#5fcfb3;
  --teal-light:#a8e6d5;
  --teal-text:#4cc2a5;
  --ink:#111;
  --paper:#f4f4f4;
  --stage:#2b2b2b;
  --grey-line:#bdbdbd;
}
*{box-sizing:border-box;margin:0;padding:0}
html,body{width:991px;height:1200px;overflow:hidden;background:var(--stage)}
body{position:relative;font-family:"Roboto Condensed",sans-serif;color:var(--ink)}
.card{position:absolute;left:116px;width:772px;height:514px;overflow:hidden;background:var(--paper)}
.card--front{top:54px}
.card--back{top:614px}
.card-bg{position:absolute;inset:0}
.abs{position:absolute}

/* front */
.kicker{left:36px;top:24px;font-family:"Exo 2",sans-serif;font-size:18px;font-weight:500}
.headline{left:36px;top:50px;font-family:"Exo 2",sans-serif;font-weight:800;font-size:43px;line-height:43px;text-transform:uppercase}
.tab{left:0;height:28px;background:var(--ink);color:#fff;border-radius:0 14px 14px 0;font-family:"Roboto Condensed",sans-serif;font-size:14px;line-height:28px;padding:0 22px 0 36px;text-transform:uppercase;white-space:nowrap}
.tab--front{top:232px;min-width:274px}
.pillars{left:36px;top:276px;width:380px}
.pillar{position:relative;height:45px;margin-bottom:4px;padding-left:53px}
.pillar-icon{position:absolute;left:0;top:0;width:40px;height:40px;border-radius:50%;background:var(--teal)}
.pillar h3{font-size:11px;font-weight:700;text-transform:uppercase;padding-top:4px}
.pillar p{font-size:10px;line-height:12.5px;color:#333}
.catchline{left:36px;top:419px;font-size:11px;font-weight:700;white-space:nowrap}
.call{font-family:"Exo 2",sans-serif;font-weight:700;font-size:36px;letter-spacing:4px;white-space:nowrap}
.call span{color:var(--teal-text)}
.call--front{left:36px;top:444px}
.contacts{font-family:"Exo 2",sans-serif;font-size:10px;white-space:nowrap}
.contacts--front{left:36px;top:484px}
.contacts b{color:var(--teal-text);font-weight:700}
.date-badge{left:450px;top:374px;width:120px;height:120px;border-radius:50%;background:var(--ink);color:#fff;text-align:center;padding-top:33px;font-family:"Roboto Condensed",sans-serif;white-space:nowrap}
.date-badge small{font-size:11px;display:block;margin-bottom:2px}
.date-badge strong{color:var(--teal);font-size:18px;line-height:21px;display:block;text-transform:uppercase;font-weight:700}
.brand-badge{border-radius:50%;background:var(--teal-light);border:6px solid #fff;display:flex;align-items:center;justify-content:center}
.brand-badge span{font-family:"Exo 2",sans-serif;font-weight:800;color:var(--ink);text-align:center;line-height:1}
.brand-badge--front{left:548px;top:270px;width:216px;height:216px}
.brand-badge--front span{font-size:34px}

/* back */
.details{left:28px;top:28px;width:330px;font-size:11.5px;line-height:15.2px}
.details b{font-weight:700}
.brand-badge--back{left:364px;top:85px;width:144px;height:144px}
.brand-badge--back span{font-size:23px}
.stamp{left:664px;top:26px;width:86px;height:103px;border:1px solid #999;background:#fff;font-size:12px;font-weight:700;color:#333;text-align:center;padding-top:36px;line-height:15px}
.address-line{left:522px;width:228px;height:1px;background:var(--grey-line)}
.investment{left:28px;top:220px;font-size:16.5px;line-height:21.5px;font-weight:700}
.investment span{color:var(--teal-text)}
.tab--back{top:300px;min-width:242px;padding-left:27px}
.mentor-photo{width:76px;height:76px;border-radius:50%;border:3px solid #fff;background:linear-gradient(#9a9a9a,#d6d6d6);box-shadow:0 0 0 1px #ccc}
.mentor{font-size:9px;line-height:10.5px;color:#333;width:90px}
.mentor h4{font-size:12px;font-weight:700;color:var(--ink);margin-bottom:3px;text-transform:uppercase}
.call--back{left:28px;top:446px;color:#fff}
.contacts--back{left:28px;top:488px;color:#fff}
</style>
</head>
<body>

<section class="card card--front">
  <svg class="card-bg" width="772" height="514" viewBox="0 0 772 514">
    <defs>
      <linearGradient id="frontTeal" x1="0" y1="0" x2="1" y2="0">
        <stop offset="0" stop-color="#6fd3bb"/><stop offset="1" stop-color="#a6e5d5"/>
      </linearGradient>
      <linearGradient id="scene" x1="0" y1="0" x2="1" y2="1">
        <stop offset="0" stop-color="#1a1a1a"/><stop offset=".55" stop-color="#4a4a4a"/><stop offset="1" stop-color="#b88424"/>
      </linearGradient>
    </defs>
    <rect width="772" height="514" fill="#f2f2f2"/>
    <path d="M0 0H772V170C560 170 320 180 0 210Z" fill="url(#frontTeal)"/>
    <circle cx="546" cy="242" r="236" fill="#c6efe4"/>
    <circle cx="546" cy="242" r="206" fill="url(#scene)" role="img" aria-label="Illustration: a row of grey figures with one orange woman figure stepping out of line"/>
  </svg>

  <p class="abs kicker">Leadership Specialist Boutique</p>
  <h1 class="abs headline">Launching a<br>Residential<br>Womans<br>Workshop</h1>
  <div class="abs tab tab--front">The Core Philosophy of the Program</div>

  <div class="abs pillars">
    <div class="pillar">
      <svg class="pillar-icon" viewBox="0 0 40 40"><circle cx="20" cy="20" r="20" fill="#5fcfb3"/><circle cx="20" cy="20" r="10" fill="#111"/><path d="M10 20h20M20 10c-5 6-5 14 0 20M20 10c5 6 5 14 0 20" stroke="#5fcfb3" stroke-width="1.2" fill="none"/></svg>
      <h3>Worldview</h3><p>A view Held inside of us as to how things work</p>
    </div>
    <div class="pillar">
      <svg class="pillar-icon" viewBox="0 0 40 40"><circle cx="20" cy="20" r="20" fill="#5fcfb3"/><path d="M20 10v19M12 14h16M14 29h12" stroke="#111" stroke-width="1.6" fill="none"/><path d="M9 22l3-8 3 8zM25 22l3-8 3 8z" fill="#111"/></svg>
      <h3>Biases</h3><p>Our own behaviours and the behaviours of others<br>that reinforce this worldviews</p>
    </div>
    <div class="pillar">
      <svg class="pillar-icon" viewBox="0 0 40 40"><circle cx="20" cy="20" r="20" fill="#5fcfb3"/><rect x="10" y="13" width="19" height="13" rx="1" fill="none" stroke="#111" stroke-width="1.6"/><path d="M19 26v4M15 30h9" stroke="#111" stroke-width="1.6"/><circle cx="28" cy="12" r="5" fill="#111"/></svg>
      <h3>Error Scripts</h3><p>Stories implanted by us or others that limits our potential</p>
    </div>
  </div>

  <p class="abs catchline">Rewiting a new Personal Narrative allows us to shatter our own glass celing.</p>
  <p class="abs call call--front">CALL: <span>0419372605</span></p>
  <p class="abs contacts contacts--front"><b>➤</b> brightpathforwardgroup.com.au | <b>●</b> info@brightpathforwardgroup.com.au.</p>

  <div class="abs date-badge"><small>2 ½ Days Residential</small><strong>26th to 28th<br>May 2019</strong></div>
  <div class="abs brand-badge brand-badge--front"><span>Bright<br>Path</span></div>
</section>

<section class="card card--back">
  <svg class="card-bg" width="772" height="514" viewBox="0 0 772 514">
    <defs>
      <linearGradient id="backTeal" x1="0" y1="0" x2="1" y2="0">
        <stop offset="0" stop-color="#6fd3bb"/><stop offset="1" stop-color="#9fe2d1"/>
      </linearGradient>
    </defs>
    <rect width="772" height="514" fill="#f2f2f2"/>
    <rect width="772" height="206" fill="url(#backTeal)"/>
    <path d="M0 434H500L560 514H0Z" fill="#151515"/>
    <circle cx="857" cy="257" r="466" fill="#dcdcdc"/>
    <circle cx="857" cy="257" r="453" fill="#fff"/>
  </svg>

  <div class="abs details">
    <b>Program and Upcoming Dates</b> :<br>
    2 ½ Days residential – 26th to 28th May 2019<br>
    <b>May Venue</b> :&nbsp; The Larchmont Retreat, Glenrowan NSW<br>
    <b>Future Programs</b> :&nbsp; August, October, March<br>
    <b>Why</b> : The program is emersive and wholistic which includes development of your life and leadership skills, by rewriting your narrative and a personal action plan for change<br>
    <b>Support &amp; Program Inclusions</b> :<br>
    LSI Assessment, leadership skills sessions, indevidual coaching sessions, guest speakers, body wellness therapists as well as accomodation and all meals are included
  </div>

  <div class="abs brand-badge brand-badge--back"><span>Bright<br>Path</span></div>

  <div class="abs stamp">STAMP<br>HERE</div>
  <div class="abs address-line" style="top:212px"></div>
  <div class="abs address-line" style="top:259px"></div>
  <div class="abs address-line" style="top:301px"></div>
  <div class="abs address-line" style="top:349px"></div>

  <p class="abs investment">Investment for May 2019 Program :<br>
    <span>$3,495</span> (Early Bird Book by 26th April) <span>$3,095</span><br>
    Quote QBR <span>Code 9455</span> for a further <span>$100</span> Discount</p>

  <div class="abs tab tab--back">Program Mentors and Founders</div>

  <div class="abs mentor-photo" style="left:32px;top:342px" role="img" aria-label="Portrait photo of mentor Dana Whitlock"></div>
  <div class="abs mentor" style="left:122px;top:354px"><h4>Dana Whitlock</h4>An intuitive advisor<br>to empowered<br>women</div>
  <div class="abs mentor-photo" style="left:214px;top:342px" role="img" aria-label="Portrait photo of mentor Owen Hartley"></div>
  <div class="abs mentor" style="left:304px;top:354px"><h4>Owen Hartley</h4>Trusted Advisor to<br>wise women</div>

  <p class="abs call call--back">CALL: <span>0419372605</span></p>
  <p class="abs contacts contacts--back"><b>➤</b> brightpathforwardgroup.com.au | <b>●</b> info@brightpathforwardgroup.com.au.</p>
</section>

</body>
</html>
```